Photo Storage Service - Web Application

This is web design for a simple photo storage service.
There is a web page and on the left side is a list of folders and on the right side there are photo thumbnails. By pressing a photo thumbnail, they will see the full size (it's just a link to a different page).
This project is limited only to ONE page, which is the page with the folders list and the thumbnails. However it contains some features that I will try to list here:
- Name of the service: Tavo Vault
- Location of account: http://username.tavo.example
- Folder list: Show all folders belonging to the user. Because you have to be able to drag photos to a folder, they have to be visible and cannot be hidden behind a menu item etc.
- Thumbnails with photos (in the future also videos)
- Adjusted view with smaller thumbnails and less space for folder list (so it is possible to view a larger quantity of thumbnails)- Select multiple thumbnails with rectangle- Show that a thumbnail is selected (maybe bold border?)
- Simple mobile view, but no emphasis on the mobile view in this design project.
- Drag one or more selected photos to a folder
- Delete one or more selected photos
- Drag a folder to another folder
- Rename folder
- Delete folder
- Create folder
- Show progress when deleting/moving (because it calls for every photo, so if there are 100 photos, it will delete 1 by 1 and it will take about 10 seconds - you could show progress bar or equivalent)
Background information: This is for a photo storage service NOT intended for sharing photos, but intended to indefinitely store photos and for yourself to browse your own photos.
It is a design requirement that it loads extremely fast. So we need to limit as much as possible extra graphics that cannot be done by CSS and other external libraries.
(I know this is ONLY design and nothing to do with CSS or libraries, but I can assess from the design if it might be heavy to load when implemented)
I have attached a crude screenshot of the current design, just for your understanding. It should not match this design and you are not in any way supposed to FIT your design into this same style or structure.
Target Market(s)
Consumers
Number of Pages Required
1 page
Font styles to use
Look and feel
Each slider illustrates characteristics of the customer's brand and the style your logo design should communicate.

```html
<!DOCTYPE html>
<html lang="en">
<head>
<meta charset="utf-8">
<title>Tavo Vault – Photos</title>
<link href="https://fonts.googleapis.com/css2?family=Open+Sans:wght@400;600&display=swap" rel="stylesheet">
<style>
:root{
  --sidebar:#454c66;
  --sidebar-text:#a9afc2;
  --white:#ffffff;
  --accent:#33a9e0;
  --ink:#3d4150;
  --muted:#9aa0ad;
  --line:#eef0f3;
  --selected-bg:#f7f7f8;
  --selected-border:#e9eaee;
  --chip:#454c66;
}
*{box-sizing:border-box;margin:0;padding:0}
html,body{width:1200px;height:1132px;overflow:hidden;background:var(--white);font-family:"Open Sans",Arial,sans-serif;color:var(--ink)}
.app{position:relative;width:1200px;height:1132px}

/* Sidebar */
.sidebar{position:absolute;left:0;top:0;width:224px;height:1132px;background:var(--sidebar)}
.brand{position:absolute;left:0;top:30px;width:196px;text-align:center}
.brand-dot{display:block;width:36px;height:36px;border-radius:50%;background:var(--accent);margin:0 auto 12px}
.brand-name{font-size:16px;color:var(--sidebar-text);font-weight:400}
.file-tab{position:absolute;left:24px;top:133px;font-size:13px;font-weight:600;color:var(--white)}
.file-add{position:absolute;left:156px;top:133px;width:17px;height:17px}
.tab-track{position:absolute;left:24px;top:164px;width:149px;height:3px;background:#5b6280}
.tab-track span{display:block;width:74px;height:3px;background:var(--accent)}
.upload-btn{position:absolute;left:16px;top:196px;width:166px;height:35px;border:1px solid var(--accent);border-radius:2px;color:var(--white);font-size:14px;display:flex;align-items:center;padding-left:52px}
.upload-btn svg{position:absolute;left:13px;top:11px}
.folders{position:absolute;left:18px;top:270px;list-style:none}
.folders li{height:45px;font-size:14px;color:var(--sidebar-text);line-height:22px}

/* Header */
.topbar{position:absolute;left:224px;top:0;width:940px;height:66px;border-bottom:1px solid var(--line)}
.search{position:absolute;left:34px;top:23px;display:flex;align-items:center;gap:6px;font-size:13px;color:#c7cad2}
.user{position:absolute;left:750px;top:22px;display:flex;align-items:center;gap:14px;font-size:13px;color:var(--ink)}

/* Main */
.tabs{position:absolute;left:259px;top:88px;display:flex;gap:26px;font-size:20px}
.tabs .active{color:var(--ink)}
.tabs .inactive{color:#c9ccd5}
.tools{position:absolute;left:262px;top:140px;display:flex;gap:15px}
.tooltip{position:absolute;left:253px;top:171px;width:53px;height:23px;border:1px solid #dcdfe5;border-radius:2px;font-size:12px;color:#5b6072;text-align:center;line-height:21px;background:var(--white)}
.sort{position:absolute;left:977px;top:139px;display:flex;align-items:center;font-size:12px;color:#7b8193}
.sort .on{width:55px;height:23px;border-radius:2px;background:var(--chip);color:var(--white);text-align:center;line-height:23px;font-weight:600}
.sort .size{margin-left:32px}
.sort .mod{margin-left:34px}
.rule{position:absolute;left:259px;top:178px;width:903px;height:1px;background:var(--line)}

.grid{position:absolute;left:259px;top:219px;display:grid;grid-template-columns:repeat(5,164px);column-gap:20px;grid-template-rows:230px 225px 188px auto}
.tile{position:relative}
.tile.is-selected::before{content:"";position:absolute;left:-6px;top:-8px;width:178px;height:198px;background:var(--selected-bg);border:1px solid var(--selected-border);border-radius:2px}
.thumb{position:relative;width:164px;height:132px}
.is-selected .thumb::after{content:"";position:absolute;inset:0;background:rgba(20,20,20,.55)}
.check{position:absolute;right:7px;top:12px;z-index:2}
.play{position:absolute;left:66px;top:50px}
.band{position:absolute;left:0;bottom:0;width:164px;height:14px;background:rgba(255,255,255,.45)}
.name{position:relative;margin-top:8px;font-size:13px;color:var(--ink)}
.size-label{position:relative;margin-top:4px;font-size:12px;color:var(--muted)}

.p-clown{background:radial-gradient(circle at 62% 50%,#f07a1a 0,#c85a0f 30%,#3e2a1c 70%)}
.p-train{background:linear-gradient(160deg,#4a4441,#2a2624)}
.p-friends{background:linear-gradient(180deg,#c9c0a6 0,#7c6a4f 55%,#5a4530)}
.p-wonderful{background:linear-gradient(180deg,#6f6c6a 0,#c9995a 30%,#4f5a32 60%,#3e4a25)}
.p-gymnast{background:radial-gradient(circle at 55% 50%,#e2b7b3 0,#b65670 40%,#6e6058 80%)}
.p-dandelion{background:radial-gradient(circle at 60% 55%,#8fd0ef 0,#2a8ccc 45%,#0f4f85)}
.p-poppy{background:radial-gradient(circle at 55% 40%,#d62a1c 0,#a6a23c 35%,#6f7a2e 80%)}
.p-droplets{background:radial-gradient(circle at 40% 50%,#a7c25a 0,#6b8c2a 50%,#3f5818)}
.p-daisy{background:linear-gradient(180deg,#3c4a66 0,#5a5550 60%,#a7a29c)}
.p-sunshine{background:radial-gradient(circle at 45% 55%,#f1c9a6 0,#d8a680 40%,#6d5e4e 85%)}
.p-bike{background:linear-gradient(135deg,#d47aa8,#6a4fa6 50%,#e5a86a)}
.p-glasses{background:radial-gradient(circle at 50% 45%,#234a8a 0,#101b33 55%,#0c1220)}
.p-road{background:linear-gradient(180deg,#6f6a63,#b38a6a 55%,#4b4a4d)}
.p-bottle{background:radial-gradient(circle at 55% 50%,#c27b1c 0,#5b4221 45%,#221a12)}
.p-camera{background:radial-gradient(circle at 60% 60%,#3a3532 0,#7a4a24 55%,#24201c)}
</style>
</head>
<body>
<div class="app">
  <aside class="sidebar">
    <div class="brand"><span class="brand-dot"></span><span class="brand-name">Tavo Vault</span></div>
    <div class="file-tab">File Name</div>
    <svg class="file-add" viewBox="0 0 18 18"><circle cx="9" cy="9" r="8" fill="none" stroke="#33a9e0" stroke-width="1"/><path d="M9 5v8M5 9h8" stroke="#33a9e0" stroke-width="1"/></svg>
    <div class="tab-track"><span></span></div>
    <div class="upload-btn"><svg width="12" height="13" viewBox="0 0 12 13"><path d="M6 12V1M1.5 5.5 6 1l4.5 4.5" fill="none" stroke="#33a9e0" stroke-width="1.2"/></svg>Upload Files</div>
    <ul class="folders">
      <li>Inbox</li><li>80s party</li><li>A day in oslo</li><li>A tour of Sevenborg</li><li>Alicante 2018</li><li>Alicante after christmas</li><li>Bandarban</li><li>Mobile Uploads</li><li>Random</li><li>Recently upload photo</li><li>Sundarban</li><li>tea garden</li>
    </ul>
  </aside>

  <header class="topbar">
    <div class="search"><svg width="13" height="13" viewBox="0 0 13 13"><circle cx="5.5" cy="5.5" r="4.5" fill="none" stroke="#c7cad2"/><path d="M9 9l3.5 3.5" stroke="#c7cad2"/></svg>Search...</div>
    <div class="user">
      <svg width="16" height="20" viewBox="0 0 16 20"><path d="M3 14V8a5 5 0 0 1 10 0v6l1.5 2h-13z" fill="none" stroke="#33a9e0"/><path d="M6.5 18h3" stroke="#33a9e0"/></svg>
      <span>Rowan Castell</span>
      <svg width="9" height="6" viewBox="0 0 9 6"><path d="M1 1l3.5 3.5L8 1" fill="none" stroke="#c7cad2"/></svg>
    </div>
  </header>

  <nav class="tabs"><span class="active">Photos</span><span class="inactive">Videos</span></nav>

  <div class="tools">
    <svg width="20" height="22" viewBox="0 0 20 22"><path d="M5 9V1h8l4 4v15H5v-3" fill="none" stroke="#a9b0bf"/><path d="M9 9h5M9 12h5M9 15h5" stroke="#a9b0bf"/><path d="M3 21v-8M0.5 15.5 3 13l2.5 2.5" fill="none" stroke="#33a9e0"/></svg>
    <svg width="22" height="22" viewBox="0 0 22 22"><path d="M5 13V2h6l2 2h8v15H9" fill="none" stroke="#a9b0bf"/><path d="M4 15v6M1 18h6" stroke="#33a9e0"/></svg>
    <svg width="22" height="22" viewBox="0 0 22 22"><path d="M2 2h18v14h-7M9 16H2z" fill="none" stroke="#a9b0bf"/><path d="M11 21v-9M8 15l3-3 3 3" fill="none" stroke="#33a9e0"/></svg>
    <svg width="18" height="22" viewBox="0 0 18 22"><path d="M1 4h16M6 4V1h6v3M3 4v17h12V4M7 8v10M11 8v10" fill="none" stroke="#a9b0bf"/></svg>
  </div>
  <div class="tooltip">Upload</div>

  <div class="sort"><span class="on">Name</span><span class="size">Size</span><span class="mod">Modified</span></div>
  <div class="rule"></div>

  <main class="grid">
    <div class="tile"><div class="thumb p-clown" role="img" aria-label="Clownfish photo"></div><div class="name">Sad Clown.png</div><div class="size-label">3 MB</div></div>
    <div class="tile is-selected"><div class="thumb p-train" role="img" aria-label="Portrait photo, selected"></div><svg class="check" width="30" height="30" viewBox="0 0 30 30"><circle cx="15" cy="15" r="13.5" fill="none" stroke="#33a9e0" stroke-width="1.5"/><path d="M9 15.5l4 4 8-8" fill="none" stroke="#33a9e0" stroke-width="1.5"/></svg><div class="name">Waiting for the train.png</div><div class="size-label">1.5 MB</div></div>
    <div class="tile"><div class="thumb p-friends" role="img" aria-label="Two children on a wall photo"></div><div class="name">Little friends.jpg</div><div class="size-label">1.5 MB</div></div>
    <div class="tile"><div class="thumb p-wonderful" role="img" aria-label="Sunset path video"><svg class="play" width="32" height="32" viewBox="0 0 32 32"><circle cx="16" cy="16" r="15" fill="rgba(255,255,255,.2)" stroke="rgba(255,255,255,.7)" stroke-width="1.5"/><path d="M13 10v12l9-6z" fill="rgba(255,255,255,.8)"/></svg></div><div class="name">What A Wonderful.jpg</div><div class="size-label">4.5 MB</div></div>
    <div class="tile"><div class="thumb p-gymnast" role="img" aria-label="Gymnast with ball photo"></div><div class="name">Gymnast.jpg</div><div class="size-label">2 MB</div></div>

    <div class="tile"><div class="thumb p-dandelion" role="img" aria-label="Blue dandelion with droplets photo"></div><div class="name">Blue Dandelion Drops.jpg</div><div class="size-label">3 MB</div></div>
    <div class="tile"><div class="thumb p-poppy" role="img" aria-label="Red poppy photo"></div><div class="name">Poppy for Mom.png</div><div class="size-label">1.5 MB</div></div>
    <div class="tile"><div class="thumb p-droplets" role="img" aria-label="Water droplets on leaf photo"></div><div class="name">Drop some droplets.png</div><div class="size-label">1.5 MB</div></div>
    <div class="tile"><div class="thumb p-daisy" role="img" aria-label="Family feet on a log photo"></div><div class="name">Daisy.png</div><div class="size-label">4.5 MB</div></div>
    <div class="tile"><div class="thumb p-sunshine" role="img" aria-label="Smiling toddler photo"></div><div class="name">Sunshine.png</div><div class="size-label">2 MB</div></div>

    <div class="tile"><div class="thumb p-bike" role="img" aria-label="Motorbike with city lights photo"><span class="band"></span></div></div>
    <div class="tile"><div class="thumb p-glasses" role="img" aria-label="Sunglasses photo"><span class="band"></span></div></div>
    <div class="tile"><div class="thumb p-road" role="img" aria-label="Highway light trails photo"><span class="band"></span></div></div>
    <div class="tile"><div class="thumb p-bottle" role="img" aria-label="Whisky bottle photo"><span class="band"></span></div></div>
    <div class="tile"><div class="thumb p-camera" role="img" aria-label="Camera lens photo"><span class="band"></span></div></div>

    <div class="tile"><div class="thumb p-clown" role="img" aria-label="Clownfish photo"></div><div class="name">Sad Clown.png</div><div class="size-label">3 MB</div></div>
    <div class="tile is-selected"><div class="thumb p-train" role="img" aria-label="Portrait photo, selected"></div><svg class="check" width="30" height="30" viewBox="0 0 30 30"><circle cx="15" cy="15" r="13.5" fill="none" stroke="#33a9e0" stroke-width="1.5"/><path d="M9 15.5l4 4 8-8" fill="none" stroke="#33a9e0" stroke-width="1.5"/></svg><div class="name">Waiting for the train.png</div><div class="size-label">1.5 MB</div></div>
    <div class="tile"><div class="thumb p-friends" role="img" aria-label="Two children on a wall photo"></div><div class="name">Little friends.jpg</div><div class="size-label">1.5 MB</div></div>
    <div class="tile"><div class="thumb p-wonderful" role="img" aria-label="Sunset path video"><svg class="play" width="32" height="32" viewBox="0 0 32 32"><circle cx="16" cy="16" r="15" fill="rgba(255,255,255,.2)" stroke="rgba(255,255,255,.7)" stroke-width="1.5"/><path d="M13 10v12l9-6z" fill="rgba(255,255,255,.8)"/></svg></div><div class="name">What A Wonderful.jpg</div><div class="size-label">4.5 MB</div></div>
    <div class="tile"><div class="thumb p-gymnast" role="img" aria-label="Gymnast with ball photo"></div><div class="name">Gymnast.jpg</div><div class="size-label">2 MB</div></div>
  </main>
</div>
</body>
</html>
```